Business Card Design Project

The business card is for an educational company that provides personalised tuition to students.

The company logo is in orange and blue (as provided) and should be included in the name card design

The philosophy of the company is to make learning a comfortable experience for student as such design of the namecard should look fresh and has a bit of the 'wow' factor. Some of the namecard design that appeals to me are as uploaded under Sample Design.

The particulars that need to be provided are:
(1): Company Name (Quillmont Education)
(1): Name
(2): Educational qualifications which will appear below name
(3): Mobile number
(4): Email address
(5): Website

Industry/Entity Type

Business

Requirements
Must have
• (1): Company Logo

(2): The card background should preferably be coloured both for the front side and back.

(3): The choice of font is important as part of the selection consideration. There is no preferred font that I have selected, designer is free to choose the font that will complement their design.

```html
<!DOCTYPE html>
<html lang="en">
<head>
<meta charset="utf-8">
<title>Quillmont Education – Business Card</title>
<link href="https://fonts.googleapis.com/css2?family=Domine:wght@700&family=Raleway:wght@300;400&display=swap" rel="stylesheet">
<style>
  :root {
    --orange: #f36a10;
    --orange-deep: #e4711a;
    --blue: #0a7fc9;
    --blue-light: #3cc0f0;
    --ink: #3a3a3a;
    --paper: #ffffff;
    --backdrop: #ecebe8;
  }
  * { margin: 0; padding: 0; box-sizing: border-box; }
  html, body { width: 1200px; height: 900px; overflow: hidden; background: var(--backdrop); }
  .canvas { position: relative; width: 1200px; height: 900px; }

  .card { position: absolute; border-radius: 18px; overflow: hidden; box-shadow: 0 10px 30px rgba(0,0,0,0.18); }
  .card svg.art { position: absolute; inset: 0; }

  /* Front */
  .card-front { left: 90px; top: 273px; width: 620px; height: 354px; background: var(--orange); }
  .front-brand { position: absolute; left: 205px; top: 130px; display: flex; align-items: center; gap: 18px; }
  .brand-square { width: 60px; height: 60px; border-radius: 8px; background: var(--blue); }
  .front-brand .brand-name { font-family: "Domine", Georgia, serif; font-weight: 700; font-size: 44px; line-height: 1.02; color: var(--paper); }

  /* Back */
  .card-back { left: 756px; top: 140px; width: 354px; height: 620px; background: var(--paper); }
  .back-brand { position: absolute; left: 30px; top: 48px; display: flex; align-items: center; gap: 14px; }
  .back-brand .brand-square { width: 48px; height: 48px; border-radius: 7px; }
  .back-brand .brand-name { font-family: "Domine", Georgia, serif; font-weight: 700; font-size: 30px; line-height: 1.05; color: var(--ink); }

  .name-tag { position: absolute; left: 22px; top: 300px; width: 250px; padding: 14px 18px 16px; background: var(--orange-deep); border-radius: 10px; box-shadow: 3px 4px 0 rgba(0,0,0,0.25); color: var(--paper); font-family: "Raleway", Arial, sans-serif; }
  .name-tag .person { font-size: 27px; font-weight: 300; letter-spacing: 1px; text-transform: uppercase; }
  .name-tag .role { font-size: 14px; font-weight: 400; letter-spacing: 1px; text-transform: uppercase; margin-top: 2px; }

  .contact-list { position: absolute; left: 30px; top: 430px; list-style: none; font-family: "Raleway", Arial, sans-serif; font-size: 17px; font-weight: 300; color: var(--paper); }
  .contact-list li { display: flex; align-items: center; gap: 10px; margin-bottom: 14px; }
  .contact-icon { width: 20px; height: 20px; border-radius: 4px; background: var(--paper); display: flex; align-items: center; justify-content: center; }
</style>
</head>
<body>
<main class="canvas">

  <section class="card card-front" aria-label="Card front">
    <svg class="art" width="620" height="354" viewBox="0 0 620 354">
      <defs>
        <linearGradient id="sky" x1="0" y1="0" x2="1" y2="0">
          <stop offset="0" stop-color="#0a86d6"/>
          <stop offset="1" stop-color="#3cc0f0"/>
        </linearGradient>
      </defs>
      <rect class="damask-field" x="0" y="0" width="620" height="354" fill="#f36a10" role="img" aria-label="Tone-on-tone orange damask pattern"/>
      <path class="blue-wing" d="M0 0 H160 C95 70 88 140 128 182 L168 168 L150 204 C98 250 112 316 176 354 H0 Z" fill="url(#sky)"/>
      <path class="wing-edge" d="M160 0 C95 70 88 140 128 182 M150 204 C98 250 112 316 176 354" fill="none" stroke="#1a6fc0" stroke-width="6" opacity="0.5"/>
    </svg>
    <div class="front-brand">
      <div class="brand-square"></div>
      <div class="brand-name">Quillmont<br>Education</div>
    </div>
  </section>

  <section class="card card-back" aria-label="Card back">
    <svg class="art" width="354" height="620" viewBox="0 0 354 620">
      <path class="blue-field" d="M0 300 H150 Q250 300 300 200 V620 H0 Z" fill="var(--blue)"/>
      <path class="blue-swoop" d="M150 300 Q250 300 300 200" fill="none" stroke="#2aa3e6" stroke-width="8"/>
      <rect class="edge-line" x="298" y="0" width="6" height="620" fill="#1f8fd8"/>
      <rect class="orange-strip" x="304" y="0" width="50" height="620" fill="var(--orange-deep)"/>
    </svg>

    <div class="back-brand">
      <div class="brand-square"></div>
      <div class="brand-name">Quillmont<br>Education</div>
    </div>

    <div class="name-tag">
      <div class="person">Nolan Pryce</div>
      <div class="role">Project Manager</div>
    </div>

    <ul class="contact-list">
      <li>
        <span class="contact-icon">
          <svg width="14" height="14" viewBox="0 0 14 14"><path d="M3 1 L5 1 L6 4 L4.5 5 Q5.5 8 9 9.5 L10 8 L13 9 L13 11 Q13 13 11 13 Q2 12 1 3 Q1 1 3 1 Z" fill="var(--orange-deep)"/></svg>
        </span>
        0147 258 3690
      </li>
      <li>
        <span class="contact-icon">
          <svg width="14" height="14" viewBox="0 0 14 14"><circle cx="7" cy="7" r="2.6" fill="none" stroke="var(--orange-deep)" stroke-width="1.6"/><path d="M9.6 5 V8.2 Q9.6 10 11.2 10 Q12.8 10 12.8 7 A5.8 5.8 0 1 0 9.8 12" fill="none" stroke="var(--orange-deep)" stroke-width="1.6"/></svg>
        </span>
        info@quillmonteducation.com
      </li>
      <li>
        <span class="contact-icon">
          <svg width="14" height="14" viewBox="0 0 14 14"><g fill="none" stroke="var(--orange-deep)" stroke-width="1.3"><circle cx="7" cy="7" r="5.8"/><ellipse cx="7" cy="7" rx="2.6" ry="5.8"/><path d="M1.2 7 H12.8 M2.2 4 H11.8 M2.2 10 H11.8"/></g></svg>
        </span>
        www.quillmonteducation.com
      </li>
    </ul>
  </section>

</main>
</body>
</html>
```